We need UI/UX design for a public, informational website for The Harbor Lens.
The pages, structure, and content scope are already defined. Designers are required to work only on the UI/UX layout of these existing pages, focusing on clarity, hierarchy, spacing, and usability. Do not add, remove, rename, or reinterpret pages or content.
The website is strictly informational only. It must not include accounts, onboarding, payments, custody, escrow administration, marketplaces, dashboards, or any transactional functionality.
Scope of work
Apply UI/UX design to the predefined website pages
Design layout for text, images, notices, and sections
Ensure consistent components and layout patterns across page types
Optimize layouts for long form, compliance focused content
Content writing, page creation, and branding changes are out of scope.
Structure reference
The complete page list, hierarchy, and content definitions are provided in the technical documentation and must be treated as the primary source of truth.
A Figma link is provided only as a light visual reference for page existence and structure:
https://kettle-marsh-48203956.example-site.net/
Designers must rely on the documentation for in depth and authoritative reference.
Brand guidelines
The Harbor Lens has existing brand guidelines and official logos, including light and dark versions. These assets will be provided and must be followed exactly. Designers must not redesign, alter, or reinterpret the brand identity.
Look and feel direction
The desired visual direction is inspired by:
https://vantorum.example/
This reference is provided only to indicate:
Institutional and enterprise tone
Clean, modern typography
Strong hierarchy and generous whitespace
Editorial, content first layouts
Do not copy branding, layouts, components, or assets from the reference site.
Hero section direction
The hero section should follow a similar structural approach to the hero used on https://vantorum.example/
, meaning:
Strong editorial framing
Clear headline hierarchy
Calm, institutional first impression
However, the background video must be Abu Dhabi focused, not generic or global. The video should visually reflect:
Abu Dhabi skyline or architectural language
Institutional, sovereign, long term infrastructure tone
Clean, slow, cinematic motion
No promotional, marketing, or lifestyle visuals
The hero must remain informational, restrained, and credible. No hype. No calls to invest. No implied participation.
Constraints
One global primary CTA only: “Continue to Brightvault” (external)
All other interactions must be informational
No visuals or language implying offers, investment, eligibility, or participation
Clear separation between informational content and any external operational platforms
Deliverables
High fidelity UI/UX designs created in Figma, covering:
Desktop layouts
Tablet layouts where relevant
Mobile layouts
Complete Figma file(s) including:
All designed pages defined in the technical documentation
A reusable component library (headers, footers, cards, notice panels, forms, CTAs, typography styles, spacing system)
Clearly defined layout grids, spacing rules, and text styles
Proper use of components and variants, not detached frames
Designs prepared for developer handoff, including:
Clear layer naming and structure
Auto layout where appropriate
Consistent use of styles and components
Responsive behavior demonstrated within Figma
Notes or annotations only where necessary for clarity
No prototypes, interactions, or motion design beyond basic layout states, unless explicitly requested. The focus is static UI/UX clarity, not animation.
A detailed technical specification document and official brand assets will be provided.
Any designs delivered outside Figma, that alter structure or content, or that ignore the defined constraints, boundaries, or tone will be rejected.

```html
<!DOCTYPE html>
<html lang="en">
<head>
<meta charset="utf-8">
<title>The Harbor Lens — Governance &amp; Project Origination Framework</title>
<link rel="stylesheet" href="https://fonts.googleapis.com/css2?family=Archivo:wght@700;800&family=Roboto:wght@400;500;700&display=swap">
<style>
:root{
  --navy:#13182b;
  --ink:#1b1f2e;
  --text:#4a4f5c;
  --blue:#3fa3f5;
  --pale:#f1f8fc;
  --line:#e3e8ee;
  --footer:#232427;
  --white:#ffffff;
}
*{box-sizing:border-box;margin:0;padding:0}
html,body{width:1200px;height:5195px;overflow:hidden}
body{position:relative;font-family:"Roboto",sans-serif;color:var(--text);background:var(--white)}
section,header,footer{position:absolute;left:0;width:1200px}
.abs{position:absolute}
.h2{font-family:"Archivo",sans-serif;font-weight:800;color:var(--ink);font-size:38px;line-height:50px;text-transform:uppercase;letter-spacing:-.5px}
.copy{font-size:15px;line-height:28.5px;color:var(--text);text-align:justify}
.btn{display:inline-flex;align-items:center;justify-content:center;font-family:"Roboto",sans-serif;font-weight:700;font-size:12.5px;text-transform:uppercase;letter-spacing:.3px;color:var(--white);background:var(--blue);text-decoration:none}
.btn-outline{background:transparent;border:2px solid var(--white)}
.btn-dark-outline{background:var(--white);border:2px solid var(--ink);color:var(--ink);border-radius:3px}
.photo{position:absolute}

/* hero */
.hero{top:0;height:847px;background:linear-gradient(180deg,#0b1a3c 0%,#1a2f63 35%,#3b3f5e 55%,#2a2f52 70%,#1b2d52 100%)}
.hero-skyline{position:absolute;left:0;top:180px;width:1200px;height:400px;background:linear-gradient(180deg,rgba(40,50,90,0) 0%,rgba(210,160,70,.35) 55%,rgba(70,90,140,.5) 80%,rgba(20,30,60,0) 100%)}
.hero-shade{position:absolute;left:0;bottom:0;width:1200px;height:330px;background:linear-gradient(180deg,rgba(13,22,52,0),rgba(13,22,52,.85))}
.top-cta{position:absolute;left:847px;top:0;width:208px;height:40px;border-radius:0 0 3px 3px}
.brand{position:absolute;left:145px;top:38px;display:flex;align-items:center;gap:14px;color:var(--white);font-family:"Archivo",sans-serif;font-weight:700;font-size:25px;text-transform:uppercase;letter-spacing:.5px}
.brand-dot{width:22px;height:22px;border:2px solid var(--white);border-radius:50%}
.nav{position:absolute;left:512px;top:82px;display:flex;gap:25px;list-style:none}
.nav a{color:var(--white);text-decoration:none;font-size:14px}
.nav .active{border-bottom:2px solid var(--blue);padding-bottom:6px}
.hero-title{position:absolute;left:145px;top:580px;font-family:"Archivo",sans-serif;font-weight:800;font-size:38px;line-height:50px;color:var(--white);text-transform:uppercase}
.hero-lead{position:absolute;left:702px;top:582px;width:353px;font-size:14px;line-height:24.5px;color:var(--white);text-align:justify}
.hero-actions{position:absolute;left:702px;top:702px;display:flex;gap:12px}
.hero-actions .btn{height:44px;border-radius:2px}
.play{position:absolute;left:1116px;top:772px}

/* about */
.about{top:847px;height:565px}
.about .h2{position:absolute;left:145px;top:85px}
.about .copy{position:absolute;left:145px;top:155px;width:493px}
.about-photo{left:688px;top:73px;width:417px;height:417px;border-radius:50%;background:radial-gradient(circle at 40% 30%,#c9d6df,#5a9aa3 50%,#1f6f7c 80%)}

/* governance */
.governance{top:1412px;height:625px;background:var(--pale)}
.gov-a{left:83px;top:111px;width:199px;height:327px;border-radius:14px;background:linear-gradient(160deg,#6fa9dc,#9fb8c8 60%,#6a7a6a)}
.gov-b{left:297px;top:194px;width:201px;height:326px;border-radius:14px;background:linear-gradient(180deg,#3a3130,#b27d3e 60%,#e1a54b)}
.governance .h2{position:absolute;left:561px;top:155px}
.governance .copy{position:absolute;left:561px;top:286px;width:494px}

/* role */
.roles{top:2037px;height:525px;background:var(--white)}
.roles .h2{position:absolute;left:145px;top:120px}
.roles .copy{position:absolute;left:145px;top:192px;width:477px}
.roles-photo{left:710px;top:0;width:490px;height:525px;background:linear-gradient(180deg,#bfd6ea 0%,#a9c1d6 45%,#7c9cb2 65%,#3f7fa3 100%)}

/* ecosystem */
.ecosystem{top:2562px;height:746px;background:var(--pale)}
.ecosystem .h2{position:absolute;left:0;width:1200px;top:95px;text-align:center}
.eco-lead{position:absolute;left:0;width:1200px;top:170px;text-align:center;font-size:15px;color:var(--ink)}
.layer{position:absolute;border-radius:50%;background:var(--white);border:1px solid var(--line);display:flex;flex-direction:column;align-items:center;justify-content:center;text-align:center;padding:0 26px}
.layer .num{font-family:"Roboto",sans-serif;font-weight:500;font-size:34px;color:var(--ink)}
.layer .name{font-weight:500;font-size:16px;color:var(--ink);margin:6px 0 8px}
.layer p{font-size:12.5px;line-height:17px;color:var(--text)}
.layer.featured{box-shadow:0 10px 30px rgba(30,60,100,.14);border:none}
.layer.featured p{font-size:15px;line-height:24px}
.eco-btn{position:absolute;left:496px;top:613px;width:208px;height:43px;border-radius:2px}

/* escrow */
.escrow{top:3308px;height:1030px}
.escrow .h2{position:absolute;left:145px;top:100px}
.escrow .copy{position:absolute;left:712px;top:92px;width:343px}
.escrow-photo{left:0;top:347px;width:599px;height:492px;background:linear-gradient(180deg,#8da3ba 0%,#a9a28c 40%,#5e5a55 70%,#2e3138 100%)}
.dots{position:absolute;background-image:radial-gradient(#7c8494 1.6px,transparent 1.7px);background-size:12px 12px}
.work-card{position:absolute;left:434px;top:498px;width:621px;height:500px;background:var(--white);box-shadow:0 10px 40px rgba(20,30,50,.1)}
.work-card .h2{position:absolute;left:95px;top:98px}
.work-card p{position:absolute;left:95px;top:228px;width:380px;font-size:15px;line-height:28.5px}

/* contact */
.contact{top:4338px;height:483px}
.contact .h2{position:absolute;left:145px;top:92px}
.contact .copy{position:absolute;left:145px;top:160px;width:377px;text-align:left}
.contact-btn{position:absolute;left:145px;top:317px;width:208px;height:45px;border-radius:2px}
.field{position:absolute;border:1.5px solid #d4d8de;border-radius:3px;font-size:12.5px;color:#333;padding:14px 16px;background:var(--white)}
.submit{position:absolute;left:641px;top:316px;width:178px;height:44px}

/* footer */
.site-footer{top:4821px;height:374px;background:var(--footer);color:var(--white)}
.col-title{position:absolute;top:95px;font-family:"Archivo",sans-serif;font-weight:700;font-size:21px;text-transform:uppercase}
.links{position:absolute;list-style:none}
.links li{font-size:14.5px;line-height:28.5px}
.socials{position:absolute;left:845px;top:146px;display:flex;gap:10px}
.socials span{width:33px;height:33px;border-radius:50%;border:2px solid var(--white)}
.foot-cta{position:absolute;left:845px;top:209px;width:208px;height:43px;border-radius:2px}
.legal-line{position:absolute;left:0;width:1200px;top:315px;text-align:center;font-size:14px}
</style>
</head>
<body>

<header class="hero">
  <div class="photo hero-skyline" role="img" aria-label="Abu Dhabi skyline at dusk reflected in the water"></div>
  <div class="hero-shade"></div>
  <a class="btn top-cta" href="#">Continue to Brightvault</a>
  <div class="brand"><span class="brand-dot"></span>The Harbor Lens</div>
  <ul class="nav">
    <li><a class="active" href="#">Home</a></li>
    <li><a href="#">Framework</a></li>
    <li><a href="#">Projects</a></li>
    <li><a href="#">Brightvault</a></li>
    <li><a href="#">Insights</a></li>
    <li><a href="#">Company</a></li>
    <li><a href="#">Contact</a></li>
  </ul>
  <h1 class="hero-title">Governance &amp;<br>Project Origination<br>Framework</h1>
  <p class="hero-lead">The Harbor Lens publishes governance standards and structural concepts for complex initiatives. Operational workflows occur on a separate platform under separate terms.</p>
  <div class="hero-actions">
    <a class="btn" style="width:210px" href="#">Continue to Brightvault</a>
    <a class="btn btn-outline" style="width:208px" href="#">Learn the Framework</a>
  </div>
  <svg class="play" width="36" height="36" viewBox="0 0 36 36" aria-label="Play video"><circle cx="18" cy="18" r="17" fill="#fff"/><path d="M14 11 L25 18 L14 25 Z" fill="#13182b"/></svg>
</header>

<section class="about">
  <h2 class="h2">The Harbor Lens</h2>
  <p class="copy">The Harbor Lens is a governance and project origination group. Its purpose is to define structural standards and oversight principles for complex initiatives that may involve multiple parties, staged execution, and long-term accountability. This website publishes those standards and explains how responsibilities are separated across governance, operations, and project-level execution. This site is informational. It does not provide onboarding, account access, eligibility checks, custody of funds, escrow administration, or transaction execution. Where operational workflows exist, they are provided through a separate operating platform under separate terms and policies.</p>
  <div class="photo about-photo" role="img" aria-label="Aerial view of the Abu Dhabi corniche, flag and skyline"></div>
</section>

<section class="governance">
  <div class="photo gov-a" role="img" aria-label="Curved glass tower against a blue sky"></div>
  <div class="photo gov-b" role="img" aria-label="Illuminated towers at night"></div>
  <h2 class="h2">Governance and<br>Project Origination</h2>
  <p class="copy">Governance in this context refers to the standards that determine how projects are structured and how oversight is described. Origination refers to the initial design and definition of an initiative, including role separation, reporting expectations, and boundary setting before execution begins. The Harbor Lens focuses on these governance-level elements rather than on operating day-to-day workflows.</p>
</section>

<section class="roles">
  <h2 class="h2">Clear Role Separation</h2>
  <p class="copy">The ecosystem is designed around clear separation of responsibilities. Governance activities belong at the framework layer. Operational workflows, where available, belong on a separate operating platform designed for process execution and recordkeeping. Assets and project execution, where applicable, belong at the project level through ring-fenced structures created for specific initiatives. This separation is intended to reduce ambiguity and help stakeholders understand who is responsible for what.</p>
  <div class="photo roles-photo" role="img" aria-label="Abu Dhabi waterfront towers across the bay"></div>
</section>

<section class="ecosystem">
  <h2 class="h2">How the Ecosystem Works</h2>
  <p class="eco-lead">At a high level, the ecosystem can be understood as three layers:</p>
  <div class="layer" style="left:161px;top:280px;width:246px;height:246px">
    <div class="num">01</div><div class="name">Governance</div>
    <p>Defines standards, explains role boundaries, and publishes framework information</p>
  </div>
  <div class="layer featured" style="left:460px;top:262px;width:282px;height:282px">
    <div class="num">02</div><div class="name">Operations</div>
    <p>Manages workflow processes such as documentation steps and record-anchored audit events through a separate platform.</p>
  </div>
  <div class="layer" style="left:795px;top:280px;width:246px;height:246px">
    <div class="num">03</div><div class="name">Project Execution</div>
    <p>Occurs at the project level through dedicated structures that hold responsibilities &amp; assets where applicable.</p>
  </div>
  <a class="btn eco-btn" href="#">Learn the Framework</a>
</section>

<section class="escrow">
  <h2 class="h2">Independent Escrow<br>&amp; Milestone Oversight</h2>
  <p class="copy">Some initiatives use independent escrow arrangements to coordinate staged releases linked to milestone completion. Escrow can support execution discipline by requiring defined evidence before releases occur. Escrow does not guarantee outcomes, timelines, or success, and it is not administered by this website operator. This site describes the concept for clarity and transparency.</p>
  <div class="dots" style="left:530px;top:405px;width:120px;height:96px"></div>
  <div class="photo escrow-photo" role="img" aria-label="Dubai skyline with highways at dusk"></div>
  <div class="dots" style="left:978px;top:905px;width:120px;height:115px"></div>
  <div class="work-card">
    <h2 class="h2">Where Operational<br>Workflows Happen</h2>
    <p>Operational workflows, including any onboarding or workflow participation where permitted, occur on a separate operating platform under separate terms and policies. If you need operational access, use the Brightvault page on this site to navigate externally. This website does not host those workflows.</p>
  </div>
</section>

<section class="contact">
  <h2 class="h2">Contact &amp; Inquiries</h2>
  <p class="copy">If you have questions about governance framework concepts, role boundaries, or information published on this website, you can contact the team using the Contact page. Do not submit sensitive personal data through public forms.</p>
  <a class="btn contact-btn" href="#">Contact the Team</a>
  <div class="field" style="left:641px;top:86px;width:202px;height:46px">First Name</div>
  <div class="field" style="left:853px;top:86px;width:202px;height:46px">Last Name</div>
  <div class="field" style="left:641px;top:143px;width:202px;height:46px">Enter Email</div>
  <div class="field" style="left:853px;top:143px;width:202px;height:46px">Phone</div>
  <div class="field" style="left:641px;top:200px;width:414px;height:104px">Message</div>
  <a class="btn btn-dark-outline submit" href="#">Submit Message</a>
</section>

<footer class="site-footer">
  <div class="col-title" style="left:145px">Links</div>
  <ul class="links" style="left:145px;top:133px"><li>Framework</li><li>Projects</li><li>Brightvault</li><li>Insights</li></ul>
  <ul class="links" style="left:266px;top:133px"><li>Company</li><li>Contact</li><li>Legal</li><li>Glossary</li></ul>
  <div class="col-title" style="left:426px">Legal</div>
  <ul class="links" style="left:426px;top:133px"><li>Legal</li><li>Terms of Use</li><li>Privacy Policy</li><li>Cookie Policy</li></ul>
  <ul class="links" style="left:571px;top:133px"><li>Disclaimer &amp; Risk Notices</li><li>Acceptable Use Policy</li><li>Accessibility Statement</li></ul>
  <div class="col-title" style="left:845px">Social Media</div>
  <div class="socials" aria-label="Social media links"><span></span><span></span><span></span><span></span><span></span></div>
  <a class="btn foot-cta" href="#">Continue to Brightvault</a>
  <p class="legal-line">© 2026 Companyname All Rights Reserved &nbsp;|&nbsp; Privacy Policy &nbsp;|&nbsp; Terms of use</p>
</footer>

</body>
</html>
```